Brookfen 14 Industrial Park Needs Website

We are looking for a website for a new project we are working on.
Project does not have a logo so just use text. Needs to be responsive and mobile friendly for all browsers and coded for both Android & IOS. SEO is also important. Want something visually grabbing that displays growth, quality and confidence.
WordPress or Joomla – must be desktop and mobile friendly with fast page load speed. Need the ability to edit ourselves.
See attached website brief for further information.
Industry/Entity Type
Land Sale/Lease/Development
Coding
Coded - Design and coding required
Number of Pages Required
4 page
Look and feel
Each slider illustrates characteristics of the customer's brand and the style your logo design should communicate.

```html
<!DOCTYPE html>
<html lang="en">
<head>
<meta charset="utf-8">
<title>Brookfen 14 Industrial Park</title>
<link rel="stylesheet" href="https://fonts.googleapis.com/css2?family=Poppins:wght@400;500;600;700;800&display=swap">
<style>
:root{
  --navy:#0c2f66;
  --blue:#1466b8;
  --ink:#2b2f38;
  --muted:#5c6470;
  --pale:#e7eef7;
  --white:#ffffff;
  --line:#cfd8e4;
}
*{box-sizing:border-box;margin:0;padding:0}
html,body{width:1200px;height:3200px;overflow:hidden;background:var(--white)}
body{font-family:"Poppins",sans-serif;color:var(--ink);position:relative}

.site-header{position:absolute;top:0;left:0;width:1200px;height:100px;background:var(--white);z-index:5}
.brand{position:absolute;left:64px;top:18px;color:var(--navy);font-weight:700;line-height:1.05}
.brand-name{font-size:34px;display:block}
.brand-sub{font-size:17px;display:block;margin-top:4px}
.main-nav{position:absolute;right:70px;top:36px;display:flex;gap:10px;align-items:center}
.main-nav a{font-size:15px;font-weight:600;color:var(--navy);text-decoration:none;padding:10px 18px;border-radius:22px;position:relative}
.main-nav a.active{background:var(--blue);color:var(--white)}
.main-nav a.active::after{content:"";position:absolute;left:50%;bottom:-8px;margin-left:-7px;border:7px solid transparent;border-top-color:var(--blue);border-bottom:0}

.hero{position:absolute;top:100px;left:0;width:1200px;height:560px}
.hero-photo{position:absolute;inset:0;background:linear-gradient(180deg,#9fb3c4 0%,#8a9b8a 30%,#6f7f5c 60%,#4e5e3e 100%)}
.hero-shade{position:absolute;inset:0;background:rgba(10,25,50,.28)}
.hero-copy{position:absolute;top:140px;left:0;width:1200px;text-align:center;color:var(--white)}
.hero-copy h1{font-size:58px;font-weight:800;letter-spacing:1px;line-height:1.1}
.hero-copy p{font-size:31px;font-weight:700;margin-top:6px;line-height:1.1}
.btn{display:inline-block;background:var(--blue);color:var(--white);font-weight:600;font-size:15px;padding:14px 34px;border-radius:28px;text-decoration:none}
.hero .btn{margin-top:34px}
.slider-dots{position:absolute;bottom:40px;left:0;width:1200px;display:flex;justify-content:center;gap:12px}
.slider-dots span{width:34px;height:4px;background:rgba(255,255,255,.6)}
.slider-dots span.on{background:var(--white)}

.section-kicker{font-size:46px;font-weight:700;color:var(--navy);line-height:1.08}
.kicker-line{display:flex;align-items:center;gap:20px;white-space:nowrap}
.kicker-line.accent{color:var(--blue)}
.title-rule{flex:none;height:3px;background:var(--blue)}

.about{position:absolute;top:660px;left:0;width:1200px;height:520px}
.about-map{position:absolute;left:72px;top:64px;width:520px;height:380px;background:linear-gradient(135deg,#dfe8ee,#c9dbe8 50%,#e4ecd9);border:1px solid var(--line)}
.about-text{position:absolute;left:620px;top:60px;width:500px}
.about-text p{font-size:15px;line-height:1.75;color:var(--muted);margin-top:22px}
.about-text .btn{margin-top:28px}

.why{position:absolute;top:1180px;left:0;width:1200px;height:980px;background:var(--pale)}
.why h2{text-align:center;font-size:46px;font-weight:700;color:var(--navy);padding-top:80px}
.why h2 .accent{color:var(--blue)}
.feature{position:absolute;width:512px;height:340px}
.feature-photo{position:absolute;inset:0}
.feature-label{position:absolute;bottom:-26px;left:54px;width:404px;height:62px;background:var(--white);color:var(--blue);font-weight:700;font-size:21px;text-align:center;line-height:1.15;display:flex;align-items:center;justify-content:center;box-shadow:0 4px 14px rgba(0,0,0,.08)}
.feature-label.tall{height:78px;bottom:-40px}

.appraisal{position:absolute;top:2160px;left:0;width:1200px;height:600px}
.plan{position:absolute;left:344px;top:76px;width:784px;height:470px;background:linear-gradient(135deg,#5e6b58,#8b9a86 50%,#6a7a66)}
.appraisal-card{position:absolute;left:48px;top:130px;width:390px;height:360px;background:var(--white);padding:34px 24px 0 26px}
.appraisal-card .section-kicker{font-size:42px}
.appraisal-card p{font-size:14px;line-height:1.7;color:var(--muted);margin-top:22px}
.appraisal-card .btn{margin-top:26px}

.contact-band{position:absolute;top:2768px;left:0;width:1200px;height:232px;background:linear-gradient(160deg,#284a78,#17335e 55%,#0f2547)}
.contact-band h2{text-align:center;color:var(--white);font-size:44px;font-weight:700;padding-top:52px}
.contact-band .rule{width:150px;height:3px;background:var(--white);margin:12px auto 0}
.contact-email{display:flex;justify-content:center;align-items:center;gap:12px;color:var(--white);font-size:22px;font-weight:600;margin-top:18px}

.site-footer{position:absolute;top:3000px;left:0;width:1200px;height:200px;text-align:center}
.footer-nav{display:flex;justify-content:center;gap:44px;padding-top:38px}
.footer-nav a{font-size:14px;font-weight:600;color:var(--navy);text-decoration:none}
.copyright{font-size:13px;color:var(--muted);margin-top:14px}
.social{display:flex;justify-content:center;gap:18px;margin-top:22px}
.social span{width:22px;height:22px;border-radius:50%;background:var(--navy)}
</style>
</head>
<body>

<header class="site-header">
  <div class="brand"><span class="brand-name">Brookfen 14</span><span class="brand-sub">Industrial Park</span></div>
  <nav class="main-nav">
    <a class="active" href="#">HOME</a>
    <a href="#">WHY MARLOW RIDGE</a>
    <a href="#">LOT LAYOUT</a>
    <a href="#">CONTACT US</a>
  </nav>
</header>

<section class="hero">
  <div class="hero-photo" role="img" aria-label="Aerial view of the industrial park land and highway interchange"></div>
  <div class="hero-shade"></div>
  <div class="hero-copy">
    <h1>WELCOME TO BROOKFEN 14</h1>
    <p>WE ARE AN INDUSTRIAL PARK. WE ARE INTO LAND<br>SALE/LEASE/DEVELOPMENT</p>
    <a class="btn" href="#">LEARN MORE</a>
  </div>
  <div class="slider-dots"><span class="on"></span><span></span><span></span></div>
</section>

<section class="about">
  <div class="about-map" role="img" aria-label="Regional map showing the park location near Marlow Ridge"></div>
  <div class="about-text">
    <h2 class="section-kicker">
      <span class="kicker-line">ABOUT</span>
      <span class="kicker-line accent">BROOKFEN 14<span class="title-rule" style="width:120px"></span></span>
    </h2>
    <p>The property is located on the west side of the Town of Marlow Ridge, a growing municipality located northeast of Kestrel City, with a regional population of 12,649. The area has a very strong local economy due to its location between Kestrel City and Fenwater, but with a stronger agricultural base. It serves as the focal point for the Smoky Lake area, with an unemployment rate of 5.0% lower than the provincial average of 8.2%.</p>
    <a class="btn" href="#">LEARN MORE</a>
  </div>
</section>

<section class="why">
  <h2>WHY <span class="accent">MARLOW RIDGE?</span></h2>
  <div class="feature" style="left:72px;top:180px">
    <div class="feature-photo" role="img" aria-label="Town skyline by the river" style="background:linear-gradient(180deg,#8fb2d6,#6f8f6a 60%,#4f6b4a)"></div>
    <div class="feature-label">LOCATION ADVANTAGE</div>
  </div>
  <div class="feature" style="left:616px;top:180px">
    <div class="feature-photo" role="img" aria-label="Aerial view of construction in progress" style="background:linear-gradient(180deg,#b8c4cc,#b9a98c 55%,#8d8170)"></div>
    <div class="feature-label">DEVELOPMENT PLANS</div>
  </div>
  <div class="feature" style="left:72px;top:564px">
    <div class="feature-photo" role="img" aria-label="Timber framed condominium buildings under construction" style="background:linear-gradient(180deg,#9ab8d6,#c69a6a 55%,#8e6a48)"></div>
    <div class="feature-label tall">INDUSTRIAL CONDOMINIUM<br>COMPLEX</div>
  </div>
  <div class="feature" style="left:616px;top:564px">
    <div class="feature-photo" role="img" aria-label="Worker in safety vest beside shipping containers" style="background:linear-gradient(180deg,#a9c7e0,#d8b84a 55%,#9c8a4a)"></div>
    <div class="feature-label">EXISTING SHOP</div>
  </div>
</section>

<section class="appraisal">
  <div class="plan" role="img" aria-label="Aerial lot layout plan with numbered parcels"></div>
  <div class="appraisal-card">
    <h2 class="section-kicker">
      <span class="kicker-line">APPRAISAL<span class="title-rule" style="width:60px"></span></span>
      <span class="kicker-line accent">LOT LAYOUT</span>
    </h2>
    <p>This Area Structure Plan is preliminary and will require modification. Provincial Transportation is considering our proposal for access to the property off Range Road 140 to alleviate significant costs related to access from highway 14.</p>
    <a class="btn" href="#">LEARN MORE</a>
  </div>
</section>

<section class="contact-band" role="img" aria-label="Industrial warehouse building at dusk">
  <h2>CONTACT US</h2>
  <div class="rule"></div>
  <div class="contact-email">
    <svg width="24" height="18" viewBox="0 0 24 18" aria-hidden="true"><rect x="1" y="1" width="22" height="16" rx="2" fill="none" stroke="#fff" stroke-width="2"/><path d="M2 2l10 8 10-8" fill="none" stroke="#fff" stroke-width="2"/></svg>
    <span>info@brookfen14.com</span>
  </div>
</section>

<footer class="site-footer">
  <nav class="footer-nav">
    <a href="#">HOME</a><a href="#">WHY MARLOW RIDGE</a><a href="#">LOT LAYOUT</a><a href="#">CONTACT US</a>
  </nav>
  <p class="copyright">Copyright © 2024 Company Name All Rights Reserved</p>
  <div class="social"><span></span><span></span><span></span><span></span></div>
</footer>

</body>
</html>
```